" Atendimento médico em consultório/Clinica para mulheres em geral. A clinica contará com três médicas ginecologistas. Inicialmente somente a Dra. Lívia atenderá. O principal valor da Clinica é com o cuidado com a Mulher através de atendimento individual e cuidadoso através de especialistas nas áreas da ginecologia e Obstetricia. Apesar de possuir atendimento Obstétrico, o mesmo não será o principal foco da clinica. "

```html
<!DOCTYPE html>
<html lang="pt-BR">
<head>
<meta charset="utf-8">
<title>Ginecologia Aurora – Cartão da Gestante</title>
<link href="https://fonts.googleapis.com/css2?family=Crimson+Text:wght@400;600&family=Open+Sans:wght@400;600&display=swap" rel="stylesheet">
<style>
  :root{
    --rose:#ec6a73;
    --rose-mid:#ef858d;
    --rose-pale:#f8c7cb;
    --rose-soft:#fbe2e4;
    --grey-text:#9a9a9a;
    --gap:#4b4b4b;
    --white:#ffffff;
  }
  *{box-sizing:border-box;margin:0;padding:0}
  html,body{width:1200px;height:1200px;overflow:hidden;background:var(--white)}
  body{position:relative;font-family:"Open Sans",Arial,sans-serif}

  .back-panel{position:absolute;left:0;top:0;width:396px;height:828px;background:var(--rose);overflow:hidden}
  .notes-box{position:absolute;left:-40px;top:48px;width:371px;height:372px;background:var(--white);border-radius:30px}
  .notes-title{position:absolute;left:-300px;top:56px;width:500px;text-align:right;color:var(--rose);font-size:34px}
  .alert-title{position:absolute;left:-210px;top:434px;white-space:nowrap;color:var(--white);font-size:38px;font-weight:600}
  .alert-list{position:absolute;left:-170px;top:500px;list-style:none;color:var(--white);font-size:22px;line-height:40px;white-space:nowrap}
  .contact-row{position:absolute;left:10px;top:780px;display:flex;gap:22px;color:var(--white);font-size:14px;align-items:center}
  .contact-row span{display:flex;align-items:center;gap:6px}
  .contact-dot{width:14px;height:14px;border-radius:50%;background:var(--white)}
  .back-rule{position:absolute;left:0;top:816px;width:396px;height:3px;background:var(--white)}

  .cover-panel{position:absolute;left:396px;top:0;width:804px;height:828px;background:var(--white);border-top:4px solid var(--rose);border-bottom:12px solid var(--rose)}
  .cover-edge{position:absolute;right:0;top:0;width:18px;height:828px;background:var(--rose)}
  .brand-symbol{position:absolute;left:290px;top:80px;width:190px;height:190px;border-radius:50%;background:var(--rose-soft)}
  .brand-name{position:absolute;left:0;width:786px;top:330px;text-align:center;font-family:"Crimson Text",Georgia,serif;color:var(--rose);font-size:64px;line-height:1}
  .doctor-name{position:absolute;left:0;width:786px;top:412px;text-align:center;font-family:"Crimson Text",Georgia,serif;color:var(--grey-text);font-size:43px;line-height:1}
  .field{position:absolute;left:60px;width:689px;height:45px;border:2px solid var(--rose);border-radius:10px}
  .field-label{position:absolute;top:-10px;background:var(--white);padding:0 4px;color:var(--rose);font-size:13px;line-height:16px}

  .fold-gap{position:absolute;left:0;top:840px;width:1200px;height:30px;background:linear-gradient(var(--gap),#6a6a6a)}

  .record-table{position:absolute;left:0;top:870px;width:1200px;height:330px;background:var(--white)}
  .record-table .edge{position:absolute;right:0;top:0;width:24px;height:330px;background:var(--rose)}
  .header-row{position:absolute;left:0;top:18px;width:1176px;height:55px;background:var(--rose-mid)}
  .cell-head{position:absolute;top:0;height:55px;line-height:55px;text-align:center;color:var(--white);font-size:22px;border-left:2px solid var(--white)}
  .body-row{position:absolute;left:0;width:1176px;height:52px}
  .body-row.pale{background:var(--rose-pale)}
  .body-row.light{background:var(--rose-soft)}
  .col-line{position:absolute;top:18px;width:2px;height:312px;background:var(--white)}
</style>
</head>
<body>

<section class="back-panel">
  <div class="notes-box"></div>
  <p class="notes-title">Observações</p>
  <p class="alert-title">Procure o médico em caso de:</p>
  <ul class="alert-list">
    <li>Diminuição dos Movimentos do Bebê</li>
    <li>Sangramento Vaginal</li>
    <li>Perda de Líquido Vaginal</li>
    <li>Contrações Frequentes e Dolorosas</li>
  </ul>
  <div class="contact-row">
    <span><i class="contact-dot"></i>seuemail@exemplo.com</span>
    <span><i class="contact-dot"></i>Perfil Social</span>
  </div>
  <div class="back-rule"></div>
</section>

<section class="cover-panel">
  <div class="brand-symbol" role="img" aria-label="Espaço do símbolo da clínica"></div>
  <h1 class="brand-name">Ginecologia Aurora</h1>
  <p class="doctor-name">Dra. Lívia Moreno Prado</p>

  <div class="field" style="top:519px"><span class="field-label" style="left:24px">Nome da Mãe</span></div>
  <div class="field" style="top:586px"><span class="field-label" style="left:24px">Nome da Pai</span></div>
  <div class="field" style="top:653px">
    <span class="field-label" style="left:24px">Idade</span>
    <span class="field-label" style="left:260px">Plano de Saúde</span>
  </div>
  <div class="field" style="top:720px"><span class="field-label" style="left:24px">Drª</span></div>
  <div class="cover-edge"></div>
</section>

<div class="fold-gap"></div>

<section class="record-table">
  <div class="header-row">
    <div class="cell-head" style="left:0;width:48px;border-left:none"></div>
    <div class="cell-head" style="left:48px;width:115px">PA</div>
    <div class="cell-head" style="left:163px;width:113px">AU</div>
    <div class="cell-head" style="left:276px;width:108px">BCF</div>
    <div class="cell-head" style="left:384px;width:108px">MF</div>
    <div class="cell-head" style="left:492px;width:108px">EDEMA</div>
    <div class="cell-head" style="left:600px;width:120px">Data</div>
    <div class="cell-head" style="left:720px;width:456px;text-align:left;padding-left:16px">COMENTÁRIO</div>
  </div>
  <div class="body-row light" style="top:80px"></div>
  <div class="body-row pale" style="top:138px"></div>
  <div class="body-row light" style="top:196px"></div>
  <div class="body-row pale" style="top:254px"></div>
  <div class="col-line" style="left:48px"></div>
  <div class="col-line" style="left:163px"></div>
  <div class="col-line" style="left:276px"></div>
  <div class="col-line" style="left:384px"></div>
  <div class="col-line" style="left:492px"></div>
  <div class="col-line" style="left:600px"></div>
  <div class="col-line" style="left:720px"></div>
  <div class="edge"></div>
</section>

</body>
</html>
```